Sun Jubilee - Concert Poster

We need a poster for a concert involving 3 bands. Marmaduke, Auntie's Gumbo and Velveteen Ray. The event is called the Sun Jubilee. The poster will be a take away. We plan to print some to give out and some for advertising. Should be something people will want to put up on a wall. The poster should have a psychedelic "flavor", colorful.
Info. that needs to be on the poster: Sun Jubilee - Band Names - Pelham Brook's Music Hall - 4182 Route 17, Felton CA - $10 advance Tix - $12 at Door - for tickets www.pelhambrookmusic. - 21 and Over - March 21 2015 - Doors open at 7:00.

Industry/Entity Type

Event

```html
<!DOCTYPE html>
<html lang="en">
<head>
<meta charset="utf-8">
<title>Sun Jubilee – Concert Poster</title>
<link rel="stylesheet" href="https://fonts.googleapis.com/css2?family=Rye&family=Exo+2:wght@600;700&display=swap">
<style>
  :root {
    --maroon: #6a0b0d;
    --magenta: #c2185b;
    --orange: #f26b1d;
    --gold: #f7b32b;
    --violet: #5b2a86;
    --teal: #1f8a8a;
    --ink: #1a1024;
    --paper: #fffaf2;
    --backdrop: #e9e8e6;
    --psyche: linear-gradient(135deg, var(--violet) 0%, var(--magenta) 30%, var(--orange) 60%, var(--gold) 80%, var(--teal) 100%);
  }
  * { box-sizing: border-box; margin: 0; padding: 0; }
  html, body { width: 1200px; height: 1148px; overflow: hidden; background: var(--backdrop); }
  .canvas { position: relative; width: 1200px; height: 1148px; }

  .poster {
    position: absolute; left: 290px; top: 139px; width: 620px; height: 870px;
    background: var(--psyche); padding: 24px;
  }
  .poster__sheet { position: relative; width: 100%; height: 100%; background: var(--paper); }
  .poster__inner {
    position: absolute; inset: 8px;
    border: 5px solid var(--violet);
    outline: 1px solid var(--violet); outline-offset: -10px;
    display: flex; flex-direction: column; align-items: center; justify-content: space-between;
    padding: 48px 0 56px; text-align: center;
  }

  .headline { display: flex; flex-direction: column; align-items: center; }
  .title {
    font-family: "Rye", serif; font-weight: 400; line-height: 0.95;
    background: linear-gradient(180deg, var(--magenta) 0%, var(--orange) 55%, var(--gold) 100%);
    -webkit-background-clip: text; background-clip: text; color: transparent;
  }
  .title__top { display: block; font-size: 150px; letter-spacing: 8px; }
  .title__bottom { display: block; font-size: 94px; letter-spacing: 2px; }

  .lineup { list-style: none; margin-top: 26px; width: 330px; }
  .lineup li {
    display: flex; align-items: center; gap: 8px;
    font-family: "Exo 2", sans-serif; font-weight: 700; font-size: 13px;
    letter-spacing: 0.6px; text-transform: uppercase; color: var(--ink);
    line-height: 1.4;
  }
  .lineup li::before, .lineup li::after { content: ""; flex: 1; height: 2px; }
  .lineup li:nth-child(1)::before, .lineup li:nth-child(1)::after { background: var(--magenta); }
  .lineup li:nth-child(2)::before, .lineup li:nth-child(2)::after { background: var(--orange); }
  .lineup li:nth-child(3)::before, .lineup li:nth-child(3)::after { background: var(--gold); }
  .lineup li:nth-child(4)::before, .lineup li:nth-child(4)::after { background: var(--teal); }
  .lineup .lineup__join { font-size: 11.5px; }

  .venue-block { display: flex; flex-direction: column; align-items: center; }
  .venue {
    display: flex; align-items: center; gap: 12px;
    font-family: "Exo 2", sans-serif; font-weight: 700; font-size: 32px;
    color: var(--violet);
  }
  .venue__dot { width: 16px; height: 16px; border-radius: 50%; background: var(--orange); }
  .address {
    margin-top: 16px;
    font-family: "Exo 2", sans-serif; font-weight: 600; font-size: 16px; color: var(--ink);
  }

  .info { display: flex; flex-direction: column; align-items: center; }
  .prices {
    font-family: "Exo 2", sans-serif; font-weight: 700; font-size: 25px; color: var(--magenta);
  }
  .tickets {
    margin-top: 12px;
    background: linear-gradient(90deg, var(--violet), var(--magenta), var(--orange));
    color: var(--paper);
    font-family: "Exo 2", sans-serif; font-weight: 700; font-size: 19px;
    padding: 7px 20px; width: 380px;
  }
  .details {
    margin-top: 16px;
    font-family: "Exo 2", sans-serif; font-weight: 700; font-size: 25px;
    line-height: 1.12; color: var(--ink);
  }
</style>
</head>
<body>
<div class="canvas">
  <article class="poster">
    <div class="poster__sheet">
      <div class="poster__inner">
        <header class="headline">
          <h1 class="title">
            <span class="title__top">SUN</span>
            <span class="title__bottom">JUBILEE</span>
          </h1>
          <ul class="lineup">
            <li>Marmaduke</li>
            <li>Auntie's Gumbo</li>
            <li class="lineup__join">and</li>
            <li>Velveteen Ray</li>
          </ul>
        </header>

        <section class="venue-block">
          <div class="venue">
            <span class="venue__dot" aria-hidden="true"></span>
            <span class="venue__name">Pelham Brook's Music Hall</span>
          </div>
          <p class="address">4182 Route 17, Felton CA</p>
        </section>

        <section class="info">
          <p class="prices">$10 advance Tix - $12 at Door</p>
          <p class="tickets">for tickets www.pelhambrookmusic.</p>
          <p class="details">21 and Over - March 21 2015<br>Doors open at 7:00.</p>
        </section>
      </div>
    </div>
  </article>
</div>
</body>
</html>
```